Quorvane Stationery Design Project

We need stationary design that goes with the attached logo. We have logo in two different versions. One in Red/Black and the other in Blue/Green. Red/Black is going to be our primary color and we are planning to use Blue/Green occasionally as necessary.

So we need stationary design in both color combinations. Maybe you can work with Red/Black first and once we decide on the design, then you can show the Blue/Green variation.

Please see the attached png and psd files for logo.

Target Market(s)

IT departments of Medium size Enterprises.

Industry/Entity Type

Work

Requirements
Must have
• -Letter head
-Cover page design for white papers and articles that are going to publish
-Business Card
-Envelope design
Nice to have
• - High level design template that we can follow for our internal web applications

```html
<!DOCTYPE html>
<html lang="en">
<head>
<meta charset="utf-8">
<title>Quorvane Software — Business Card</title>
<link rel="stylesheet" href="https://fonts.googleapis.com/css2?family=Lato:wght@400;700;900&family=Libre+Baskerville&display=swap">
<style>
  :root {
    --page: #e6e6e6;
    --card: #ffffff;
    --ink: #111111;
    --red: #c8141c;
    --red-deep: #9e0d13;
    --muted: #333333;
  }
  * { box-sizing: border-box; margin: 0; padding: 0; }
  html, body { width: 1200px; height: 997px; overflow: hidden; }
  body {
    background: var(--page);
    font-family: "Lato", Arial, sans-serif;
    color: var(--ink);
    position: relative;
  }
  .card {
    position: absolute;
    left: 250px;
    width: 700px;
    height: 400px;
    background: var(--card);
    box-shadow: 0 6px 20px rgba(0,0,0,0.18);
    overflow: hidden;
  }
  .card--front { top: 62px; }
  .card--back { top: 534px; }

  .brand { display: flex; align-items: center; gap: 16px; }
  .brand__square { width: 22px; height: 22px; background: var(--red); }
  .brand__name {
    font-weight: 900;
    color: var(--ink);
    letter-spacing: 6px;
    text-transform: uppercase;
    line-height: 1;
  }
  .card--front .brand {
    position: absolute; left: 0; right: 0; top: 0; bottom: 0;
    justify-content: center;
  }
  .card--front .brand__name { font-size: 40px; }

  .card--back .brand { position: absolute; left: 60px; top: 70px; }
  .card--back .brand__name { font-size: 34px; }

  .holder { position: absolute; left: 120px; top: 180px; text-align: right; width: 250px; }
  .holder__name {
    font-family: "Libre Baskerville", "Times New Roman", serif;
    font-size: 24px; color: var(--ink); letter-spacing: 1px;
  }
  .holder__role {
    font-weight: 700; font-size: 16px; color: var(--red);
    letter-spacing: 0.5px; margin-top: 2px;
  }

  .divider {
    position: absolute; left: 395px; top: 160px;
    width: 2px; height: 110px;
    background: linear-gradient(to bottom, var(--red), rgba(200,20,28,0));
  }

  .contacts { position: absolute; left: 420px; top: 158px; list-style: none; }
  .contacts li {
    display: flex; align-items: center; gap: 12px;
    font-size: 15px; color: var(--muted); height: 26px;
  }
  .contacts svg { width: 16px; height: 16px; flex: none; }

  .address {
    position: absolute; left: 40px; bottom: 42px;
    font-weight: 700; font-size: 17px; color: var(--red);
  }

  .band-red {
    position: absolute; right: 0; bottom: 14px;
    width: 290px; height: 34px;
    background: linear-gradient(to bottom, var(--red), var(--red-deep));
    border-top-left-radius: 22px;
  }
  .band-black {
    position: absolute; left: 0; right: 0; bottom: 0;
    height: 14px;
    background: linear-gradient(to bottom, #3a3a3a, #050505);
  }
</style>
</head>
<body>
  <section class="card card--front" aria-label="Business card front">
    <div class="brand">
      <span class="brand__square"></span>
      <span class="brand__name">Quorvane Software</span>
    </div>
  </section>

  <section class="card card--back" aria-label="Business card back">
    <div class="brand">
      <span class="brand__square"></span>
      <span class="brand__name">Quorvane Software</span>
    </div>

    <div class="holder">
      <p class="holder__name">YOUR NAME</p>
      <p class="holder__role">DESIGNATION</p>
    </div>

    <div class="divider"></div>

    <ul class="contacts">
      <li>
        <svg viewBox="0 0 16 16" aria-hidden="true"><rect x="4" y="1" width="8" height="14" rx="1.5" fill="none" stroke="#c8141c" stroke-width="1.5"/><circle cx="8" cy="12.5" r="0.9" fill="#c8141c"/></svg>
        (555) 310-4821
      </li>
      <li>
        <svg viewBox="0 0 16 16" aria-hidden="true"><path d="M2 6c0-2 3-3 6-3s6 1 6 3l-2 1-1-2H5L4 7z" fill="#c8141c"/><rect x="3" y="8" width="10" height="6" rx="1" fill="#c8141c"/></svg>
        (555) 472-9036
      </li>
      <li>
        <svg viewBox="0 0 16 16" aria-hidden="true"><rect x="1" y="3" width="14" height="10" rx="1" fill="#c8141c"/><path d="M1.5 4l6.5 5 6.5-5" fill="none" stroke="#fff" stroke-width="1.2"/></svg>
        hello@quorvanesoftware.com
      </li>
      <li>
        <svg viewBox="0 0 16 16" aria-hidden="true"><rect x="1.5" y="6" width="8" height="4.5" rx="2.2" transform="rotate(-45 5.5 8.2)" fill="none" stroke="#c8141c" stroke-width="1.6"/><rect x="6.5" y="5.5" width="8" height="4.5" rx="2.2" transform="rotate(-45 10.5 7.8)" fill="none" stroke="#c8141c" stroke-width="1.6"/></svg>
        www.quorvanesoftware.com
      </li>
    </ul>

    <p class="address">P.O. Box 71, Halden AL, 36012</p>

    <div class="band-red"></div>
    <div class="band-black"></div>
  </section>
</body>
</html>
```